Professional Design for Rap Artist's Promotional Photos

I am promoting my new single "Loud and Sideways" by Prax. I'm a rising rap artist and am working with PR companies on major coverage right now. I need professional and inventive promotional photos to sport with the reviews, articles, and ads.

I have attached some photos I took in front of a green screen. I would like the photos touched up and the backgrounds replaced with something "Loud and Sideways"

I have attached an old Rovaldo photo that I like a lot in regards to the vibes and wacky/crazy look I'm after. He's standing in front of a cartoon background.

Industry/Entity Type

Promotional

Requirements
Must have
• green screen removal
• professional background replacement
Nice to have
• image enhancement in regards to colors, quality, contrast
Should not have
• amateur backgrounds that make the photo blatantly obvious that it is photoshopped

```html
<!DOCTYPE html>
<html lang="en">
<head>
<meta charset="utf-8">
<title>Loud and Sideways by Prax</title>
<link href="https://fonts.googleapis.com/css2?family=Luckiest+Guy&family=Arimo:wght@400&display=swap" rel="stylesheet">
<style>
  :root {
    --page: #ffffff;
    --backdrop-light: #fbfbfb;
    --backdrop-mid: #dcdcdc;
    --pattern-teal: #5fd0c8;
    --pattern-blue: #4a9fe0;
    --pattern-pale: #bfeef0;
    --stone: #a9a9a9;
    --shadow: #111111;
    --ink: #111111;
    --jacket: #8a1f4a;
    --trousers: #1a1a1a;
  }
  html, body {
    margin: 0;
    width: 1200px;
    height: 1018px;
    overflow: hidden;
    background: var(--page);
  }
  .cover {
    position: absolute;
    left: 125px;
    top: 40px;
    width: 943px;
    height: 935px;
    overflow: hidden;
    background: radial-gradient(circle at 35% 45%, var(--backdrop-light) 0%, var(--backdrop-mid) 100%);
  }
  .cover__pattern {
    position: absolute;
    inset: 0;
  }
  .cover__artist {
    position: absolute;
    left: 542px;
    top: 0;
    width: 334px;
    height: 935px;
  }
  .cover__title {
    position: absolute;
    left: 58px;
    top: 262px;
    width: 470px;
    margin: 0;
    font-family: "Luckiest Guy", "Arial Black", sans-serif;
    font-weight: 400;
    line-height: 0.95;
    white-space: nowrap;
    transform: rotate(-3deg);
    transform-origin: left top;
  }
  .cover__title-line {
    display: block;
    color: var(--stone);
    text-shadow: 7px 7px 0 var(--shadow);
  }
  .cover__title-line--top { font-size: 140px; }
  .cover__title-line--mid { font-size: 118px; padding-left: 175px; }
  .cover__title-line--bottom { font-size: 88px; }
  .cover__credit {
    position: absolute;
    left: 190px;
    top: 808px;
    margin: 0;
    font-family: "Arimo", Arial, sans-serif;
    font-size: 72px;
    font-weight: 400;
    line-height: 1;
    color: var(--ink);
  }
</style>
</head>
<body>
  <main class="cover">
    <svg class="cover__pattern" viewBox="0 0 943 935" role="img" aria-label="Geometric triangle pattern in teal and blue filling the right side of the backdrop">
      <defs>
        <linearGradient id="patternFade" x1="0" y1="0" x2="1" y2="0">
          <stop offset="0" stop-color="var(--pattern-pale)" stop-opacity="0"/>
          <stop offset="0.3" stop-color="var(--pattern-pale)" stop-opacity="0.8"/>
          <stop offset="0.7" stop-color="var(--pattern-teal)"/>
          <stop offset="1" stop-color="var(--pattern-blue)"/>
        </linearGradient>
      </defs>
      <polygon points="470,0 943,0 943,935 560,935 520,680 450,540 500,360 460,180" fill="url(#patternFade)"/>
    </svg>

    <svg class="cover__artist" viewBox="0 0 334 935" role="img" aria-label="Photo of the artist in sunglasses, a maroon velvet blazer and black jeans, holding a keyboard">
      <defs>
        <linearGradient id="artistTone" x1="0" y1="0" x2="0" y2="1">
          <stop offset="0" stop-color="#6b4a3a"/>
          <stop offset="0.22" stop-color="var(--jacket)"/>
          <stop offset="0.58" stop-color="var(--jacket)"/>
          <stop offset="0.66" stop-color="var(--trousers)"/>
          <stop offset="1" stop-color="var(--trousers)"/>
        </linearGradient>
      </defs>
      <rect x="20" y="0" width="294" height="935" rx="40" fill="url(#artistTone)" opacity="0.85"/>
    </svg>

    <h1 class="cover__title">
      <span class="cover__title-line cover__title-line--top">Loud</span>
      <span class="cover__title-line cover__title-line--mid">and</span>
      <span class="cover__title-line cover__title-line--bottom">Sideways</span>
    </h1>

    <p class="cover__credit">by Prax</p>
  </main>
</body>
</html>
```